Affiliate website design and wireframe

We need a design of an affiliate website for an application we purchased, it is important that you build the website pages according to the developer of the applications specifications (please see attached documents) the developer of the application will configure the pages and add them to the site. Please take special note of his comments below.

We all so need you to create a wire frame so the developer can test everything (http://sketchwire.tolvaro.vn/)

It will be the homepage and about 16 inner pages (please see attached files)
Here is our website http://bluvendmarket.com/affiliate/affiliates/index.php

The version of the software we purchased is the Kivo Partner Hubline version

Comments from the developers

1. I will need the source files of the design (photoshop .psd files and font files if custom fonts are used), since the implementation is closely bound to component sizes (like border width, margin width etc.) and colors. If you own a corporate design manual, it's crucial to send it as well. Also, please, make sure if you use custom fonts, that these allow legal website integration (like google web fonts).

2. Any and every content is controlled via templates. All editing/adding/removing etc. is done here. The template files are essentially html/php documents, they use a template engine called quillo (http://www.quillo.net/) which has it's own language similar to php.

3. .psd files are ideal, because we deal with the specifics of KPX/KPH implementation on a daily basis. Any html/css developed in advance may prove to be a poor choice. You may choose to let an in-house developer do the job, but experience wise this is more costly, since he will not be accustomed to the template/functionality systems of KPX/KPH.

4. I will need the source files of the design (photoshop .psd files and font files if custom fonts are used), since the implementation is closely bound to component sizes (like border width, margin width etc.) and colors. If you own a corporate design manual, it's crucial to send it as well. Also, please, make sure if you use custom fonts, that these allow legal website integration (like google web fonts).

Regards,

Dorek Hanval
Multimedia Design

We prefer illustrations more than pictures of real people.

This is the home page, it is asking for Merchant and Affiliate sign up, not just affiliate.

http://bluvendmarket.com/affiliate/index.php

Please note the home page features both Merchant and Affiliate sign up

We are looking for illustration design not just stock images

Please remember the search menu that searches for the available programs, see the example we gave you, look at the search menu at the top of the page http://www.tradelumo.com/

We are reviewing everything, no need to send more designs

Target Market(s)

Natural Products Manufacturers
Natural products Sales reps
Natural Products Bloggers
Social Marketing

Industry/Entity Type

Software

Requirements
Must have
• 1. All links on pages should go to the appropriate pages.
2. Colors can be based on our logo design (look at the attachments)
3. Here is our website http://bluvendmarket.com/affiliate/affiliates/index.php
4. We have attached a drawing of how we think the homepage concept should follow.
5. Main concept of design, is trying to show our sales people (Affiliates) are doing multiple things to advertise and sell the merchants products.(see logo)
6. Need to be able to edit all text and images.
7. Our target audience is Natural product sales people (Advertisers, bloggers, ext) and natural product manufacturers.
8. You can speak to the company who made the application, through live chat, on there website http://www.kivopartnerhubline.com/
Nice to have
• See Attached Documents.
site should take up whole website pages
Look For fun Illustrated Website, one of the better ones we have seen is http://www.tradelumo.com/index.cfm
Should not have
• Please look very carefully at developers comment above.

```html
<!DOCTYPE html>
<html lang="en">
<head>
<meta charset="utf-8">
<title>BluVend Market – Affiliate Home</title>
<link href="https://fonts.googleapis.com/css2?family=Open+Sans:wght@400;600;700&display=swap" rel="stylesheet">
<style>
:root{
  --green:#4f9a0e;
  --green-light:#6cbb1b;
  --green-dark:#3f7f0a;
  --orange:#f58a2b;
  --orange-light:#fbb268;
  --navy:#17375e;
  --text:#333;
  --muted:#555;
  --card-top:#f4f6f8;
  --card-bot:#cfd5db;
  --foot-top:#4a4a4a;
  --foot-bot:#111;
}
*{margin:0;padding:0;box-sizing:border-box}
html,body{width:949px;height:1200px;overflow:hidden;background:#fff}
body{font-family:"Open Sans",Arial,sans-serif;color:var(--text);position:relative}
.wrap{position:absolute;left:136px;width:678px}

.site-header{position:absolute;top:0;left:0;width:949px;height:105px}
.brand{position:absolute;left:136px;top:52px;display:flex;align-items:center;gap:8px;font-weight:700;font-size:20px;color:var(--green);letter-spacing:.5px}
.brand-mark{width:22px;height:22px;background:var(--navy);border-radius:50%}
.auth{position:absolute;top:61px;left:663px;display:flex;gap:4px}
.btn{display:flex;align-items:center;justify-content:center;color:#fff;font-size:13px;font-weight:600;height:31px;border-radius:3px}
.btn-login{width:73px;background:linear-gradient(var(--orange-light),var(--orange))}
.btn-signup{width:73px;background:linear-gradient(var(--green-light),var(--green))}

.main-nav{position:absolute;top:105px;left:0;width:949px;height:40px;background:linear-gradient(var(--green-light),var(--green-dark))}
.main-nav ul{list-style:none;position:absolute;left:136px;display:flex;height:40px}
.main-nav li{color:#fff;font-size:12.5px;display:flex;align-items:center;padding:0 18px;border-right:1px solid rgba(0,0,0,.2)}
.main-nav li.active{background:var(--navy);padding:0 13px}

.hero{position:absolute;top:145px;left:0;width:949px;height:394px;background:radial-gradient(ellipse at 45% 45%,#3d8fa6 0%,#2b4656 35%,#1d2630 70%,#5f6770 100%)}
.slider-ctrl{position:absolute;left:410px;top:496px;width:123px;height:20px;background:#eef0f2;border:1px solid #bbb;border-radius:3px;display:flex;align-items:center;padding-left:8px;gap:6px}
.slider-ctrl .arrows{font-size:10px;color:#333;width:28px;border-right:1px solid #bbb}
.dot{width:6px;height:6px;border-radius:50%;background:#999}
.dot.on{background:#222}

.services h2{position:absolute;top:562px;left:0;width:949px;text-align:center;font-weight:400;font-size:21px;color:var(--navy)}
.card{position:absolute;top:606px;width:161px;height:122px;background:linear-gradient(var(--card-top),var(--card-bot));border:1px solid #d6dadd;text-align:center}
.card svg{margin-top:20px}
.card p{position:absolute;top:82px;width:100%;font-size:14px;color:#333}

.join{position:absolute;top:757px;left:0;width:949px;height:132px;background:linear-gradient(#f4f7fa,#d8dde2);text-align:center}
.join h3{margin-top:9px;font-weight:400;font-size:15px;color:var(--navy)}
.join p{margin-top:13px;font-size:11.5px;color:#333}
.btn-join{position:absolute;left:410px;top:80px;width:117px;height:31px;font-size:14px;font-weight:400;background:linear-gradient(var(--green-light),var(--green-dark));border-radius:2px}

.info-col{position:absolute;top:915px;width:205px}
.info-col h4{font-size:12.5px;font-weight:600;color:var(--navy);line-height:18px;letter-spacing:.4px;margin-bottom:8px}
.info-col p{font-size:7.5px;line-height:13.5px;color:var(--muted)}

.site-footer{position:absolute;top:1042px;left:0;width:949px;height:158px;background:linear-gradient(var(--foot-top),var(--foot-bot));color:#e6e6e6}
.f-col{position:absolute;top:18px}
.f-col h5{font-size:12.5px;font-weight:400;margin-bottom:14px}
.f-col li{list-style:none;font-size:9.5px;line-height:16px}
.f-col.small li{font-size:8px}
.store{width:79px;height:25px;background:#000;border:1px solid #999;border-radius:4px;margin-top:5px}
.social li{display:flex;align-items:center;gap:10px;line-height:22px}
.sq{width:13px;height:13px;border-radius:2px}
.copy{position:absolute;left:677px;top:118px;font-size:7.5px;font-family:Arial,sans-serif}
</style>
</head>
<body>

<header class="site-header">
  <div class="brand"><span class="brand-mark"></span>BLUVEND MARKET</div>
  <div class="auth">
    <span class="btn btn-login">LOGIN</span>
    <span class="btn btn-signup">SIGN UP</span>
  </div>
</header>

<nav class="main-nav">
  <ul>
    <li class="active">HOME</li><li>ABOUT US</li><li>SERVICES</li><li>FEATURES</li><li>SUPPORT</li><li>BLOG</li><li style="border:none">CONTACT</li>
  </ul>
</nav>

<section class="hero" role="img" aria-label="Hand holding a smartphone with glowing network connections spanning a world map">
  <div class="slider-ctrl" style="top:351px">
    <span class="arrows">‹ ›</span>
    <span class="dot"></span><span class="dot"></span><span class="dot on"></span><span class="dot"></span><span class="dot"></span><span class="dot"></span>
  </div>
</section>

<section class="services">
  <h2>OUR SERVICE</h2>
  <div class="card" style="left:136px">
    <svg width="48" height="48" viewBox="0 0 48 48"><circle cx="24" cy="24" r="21" fill="none" stroke="var(--green)" stroke-width="6"/><ellipse cx="24" cy="24" rx="9" ry="21" fill="none" stroke="var(--green)" stroke-width="4" transform="rotate(35 24 24)"/></svg>
    <p>Featured service</p>
  </div>
  <div class="card" style="left:308px">
    <svg width="72" height="48" viewBox="0 0 72 48"><g fill="var(--green)"><circle cx="18" cy="14" r="8"/><path d="M4 44c0-12 6-18 14-18s14 6 14 18z"/><circle cx="54" cy="14" r="8"/><path d="M40 44c0-12 6-18 14-18s14 6 14 18z"/><circle cx="36" cy="10" r="9"/><path d="M20 44c0-14 7-20 16-20s16 6 16 20z"/></g></svg>
    <p>Featured service</p>
  </div>
  <div class="card" style="left:481px">
    <svg width="48" height="48" viewBox="0 0 48 48"><g stroke="var(--green)" stroke-linecap="round"><line x1="8" y1="8" x2="40" y2="42" stroke-width="5"/><line x1="38" y1="10" x2="10" y2="40" stroke-width="6"/></g><circle cx="38" cy="10" r="7" fill="var(--green)"/><circle cx="41" cy="7" r="3" fill="#eef1f3"/></svg>
    <p>Featured service</p>
  </div>
  <div class="card" style="left:653px">
    <svg width="58" height="48" viewBox="0 0 58 48"><g fill="none" stroke="var(--green)" stroke-width="6"><path d="M2 12h14l20 24h12"/><path d="M2 36h14l20-24h12"/></g><path d="M46 2l10 10-10 10zM46 26l10 10-10 10z" fill="var(--green)"/></svg>
    <p>Featured service</p>
  </div>
</section>

<section class="join">
  <h3>Ready to join?</h3>
  <p>Signing up and getting your account configured couldn't be easier. You can be referring business our way in as little as five minutes.</p>
  <span class="btn btn-join">JOIN NOW</span>
</section>

<section>
  <div class="info-col" style="left:137px">
    <h4>Earn up to 50% commission<br>for all products!</h4>
    <p>It couldn't be simpler! We've streamlined our entire affiliate process to ensure ease of use, while still maintaining extremely accurate affiliate tracking. The process is as follows:</p>
  </div>
  <div class="info-col" style="left:375px">
    <h4>How does it work?</h4>
    <p style="margin-top:18px">Not only can you join our team and help spread the word about your favorite products, you can get rewarded for your efforts. Our system tracks referrals and pays top commissions for every client you send our</p>
  </div>
  <div class="info-col" style="left:613px">
    <h4>High Conversion Rate<br>More Money</h4>
    <p>Our website and plans generate one of the highest conversion rates in the industry. Our high conversion rates mean that the people who you send here are more refer people here?</p>
  </div>
</section>

<footer class="site-footer">
  <div class="f-col small" style="left:136px"><h5>About us</h5><ul><li>Company</li><li>Contact us</li><li>Privacy Policy</li></ul></div>
  <div class="f-col" style="left:278px"><h5>Affiliates</h5><ul><li>Affiliates information</li><li>Affiliate link formats</li></ul></div>
  <div class="f-col" style="left:414px"><h5>Merchants</h5><ul><li>Merchants Login</li><li>Integration methods</li><li>API Reference</li><li>Samples and Tests</li><li>Kivo Partner Pro</li></ul></div>
  <div class="f-col" style="left:550px"><h5>Mobile</h5><ul><li>Get sale alerts</li></ul><div class="store"></div><div class="store"></div></div>
  <div class="f-col social" style="left:688px"><h5>Social</h5><ul>
    <li><span class="sq" style="background:#3b5b98"></span>Chatterly</li>
    <li><span class="sq" style="background:#29a9e0"></span>Chirpwave</li>
    <li><span class="sq" style="background:#d34836"></span>Circlenet</li></ul></div>
  <div class="copy">Copy Right © 2014 All rights reserved</div>
</footer>

</body>
</html>
```